GoofyJars.com - Wordpress Blog Design -

I need an overhaul of a terrible Blog design that looks like something from the early 90's. I have a Wordpress blog that needs to look large and modern so I need designers who are well versed in the WP platform. The chosen design will lead to other projects for company identity like the QZ page, Quillo and Vexly...

We write humor and sell a giant foam middle finger and a rubber dog turd...We need to stress humor but not spite.

Target Market(s)

Any man, woman or child with a sense of humor...and a credit card.

Requirements
Must have
• The site is a blog that will pass on funny stories. The site must convey humor but not spite. We like orange for whatever reason... We like our Mascot Pim the dog...
Nice to have
• Our main focus is the blog itself which will feed into social media pages. People will read the site...and buy our products.
Should not have
• We will never show a graphic or photo of our rubber dog turd.

```html
<!DOCTYPE html>
<html lang="en">
<head>
<meta charset="utf-8">
<title>GoofyJars.com — Blog</title>
<link href="https://fonts.googleapis.com/css2?family=Open+Sans:wght@400;600;700&family=Varela+Round&display=swap" rel="stylesheet">
<style>
  :root {
    --orange: #d6800a;
    --pill: rgba(255, 255, 255, 0.13);
    --white: #ffffff;
    --ink: #111111;
    --body: #2a2a2a;
    --meta: #7d7d7d;
    --coral: #f76d72;
    --rule: #e6e6e6;
    --foam-light: rgba(255, 196, 199, 0.35);
    --foam-mid: rgba(255, 185, 189, 0.55);
    --rss: #f39a1c;
  }
  * { box-sizing: border-box; margin: 0; padding: 0; }
  html, body { width: 1200px; height: 1000px; overflow: hidden; background: var(--white); }
  body { position: relative; font-family: "Open Sans", Arial, sans-serif; }

  .page { position: absolute; left: 0; top: 87px; width: 1200px; height: 779px; overflow: hidden; }

  .sidebar {
    position: absolute; left: 0; top: 0; width: 342px; height: 779px;
    background: var(--orange); font-family: "Varela Round", Arial, sans-serif; color: var(--white);
  }
  .brand { position: absolute; left: 25px; top: 128px; display: flex; align-items: center; gap: 10px; }
  .brand-dot { width: 26px; height: 26px; border-radius: 50%; background: #f6d21b; }
  .brand-name { font-size: 30px; color: #f6d21b; }
  .tagline { position: absolute; left: 25px; top: 207px; width: 300px; font-size: 12px; line-height: 17px; }
  .social { position: absolute; left: 24px; top: 266px; display: flex; gap: 10px; }
  .social-icon { width: 20px; height: 20px; border-radius: 50%; }
  .social-icon.rss { background: #f36b1c; }
  .social-icon.quillo { background: #2ea3d6; }
  .social-icon.qz { background: #56639a; }
  .nav { position: absolute; left: 25px; top: 319px; list-style: none; }
  .nav-item {
    width: 290px; height: 42px; margin-bottom: 16px; border-radius: 21px; background: var(--pill);
    display: flex; align-items: center; justify-content: space-between; padding: 0 22px; font-size: 16.5px;
  }

  .content { position: absolute; left: 421px; top: 0; width: 650px; height: 779px; }
  .product-feature {
    position: absolute; left: 99px; top: 78px; width: 340px; height: 636px; border-radius: 24px;
    background: linear-gradient(180deg, var(--foam-light), var(--foam-mid));
  }
  .tabs { position: absolute; left: 0; top: 33px; width: 650px; height: 42px; border-bottom: 2px solid var(--rule); display: flex; }
  .tab { width: 321px; text-align: center; font-size: 15.5px; line-height: 30px; }
  .tab.active { font-weight: 700; color: var(--ink); }
  .tab.topics { color: var(--coral); border-left: 1px solid var(--rule); height: 30px; }
  .tab-caret { position: absolute; left: 153px; top: 70px; }

  .post { position: absolute; left: 0; width: 650px; }
  .post-title { font-size: 27px; font-weight: 700; color: var(--ink); line-height: 36px; }
  .post-meta {
    margin-top: 6px; font-family: "Varela Round", Arial, sans-serif; font-size: 11.5px; color: var(--meta);
    display: flex; align-items: center; gap: 14px;
  }
  .post-meta .comments { display: flex; align-items: center; gap: 6px; }
  .post-excerpt { margin-top: 30px; font-family: "Varela Round", Arial, sans-serif; font-size: 11.6px; line-height: 22px; color: var(--body); }
  .post-excerpt .more { color: var(--coral); }
  .read-more {
    display: inline-flex; align-items: center; gap: 8px; margin-top: 30px; height: 35px; padding: 0 16px;
    border-radius: 18px; background: var(--coral); color: var(--white); font-size: 10px; font-weight: 700;
  }
  .post-divider { position: absolute; left: 0; top: 518px; width: 650px; border: 0; border-top: 2px solid var(--rule); }
</style>
</head>
<body>
  <div class="page">
    <aside class="sidebar">
      <div class="brand">
        <span class="brand-dot"></span>
        <span class="brand-name">GoofyJars</span>
      </div>
      <p class="tagline">We write humor and sell a giant foam middle finger and a rubber dog turd.</p>
      <div class="social">
        <span class="social-icon rss"></span>
        <span class="social-icon quillo"></span>
        <span class="social-icon qz"></span>
      </div>
      <ul class="nav">
        <li class="nav-item">Home</li>
        <li class="nav-item">Sample Page</li>
        <li class="nav-item">About Us</li>
        <li class="nav-item">Contact Us</li>
        <li class="nav-item">Multiple Paragraph Page</li>
        <li class="nav-item">Image Page</li>
        <li class="nav-item">Links Page</li>
        <li class="nav-item">RSS
          <svg width="14" height="14" viewBox="0 0 14 14" aria-hidden="true">
            <circle cx="2.5" cy="11.5" r="2" fill="var(--rss)"/>
            <path d="M1 6a7 7 0 0 1 7 7" stroke="var(--rss)" stroke-width="2" fill="none"/>
            <path d="M1 1a12 12 0 0 1 12 12" stroke="var(--rss)" stroke-width="2" fill="none"/>
          </svg>
        </li>
      </ul>
    </aside>

    <main class="content">
      <div class="product-feature" role="img" aria-label="Faint background illustration of the giant red foam hand product"></div>

      <nav class="tabs">
        <div class="tab active">ARTICLES</div>
        <div class="tab topics">TOPICS</div>
      </nav>
      <svg class="tab-caret" width="14" height="9" viewBox="0 0 14 9" aria-hidden="true">
        <path d="M2 2 L7 7 L12 2" stroke="var(--ink)" stroke-width="2.6" fill="none"/>
      </svg>

      <article class="post" style="top:186px">
        <h2 class="post-title">Headers Post</h2>
        <div class="post-meta">
          <span>August 7, 2013, admin in Uncategorized</span>
          <span class="comments">
            <svg width="11" height="10" viewBox="0 0 11 10" aria-hidden="true"><ellipse cx="5.5" cy="4.5" rx="5.5" ry="4" fill="var(--meta)"/><path d="M2 7 L1 10 L5 8 Z" fill="var(--meta)"/></svg>
            Leave a comment
          </span>
        </div>
        <p class="post-excerpt">This Is An H1 Tag Lorem ipsum dolor sit amet, consectetur adipisicing elit, sed do eiusmod tempor incididunt ut labore et dolore magna aliqua. Ut enim ad minim veniam, quis nostrud exercitation ullamco laboris nisi ut aliquip ex ea commodo consequat. This Is An H2 Tag Lorem ipsum dolor sit amet, consectetur adipisicing elit, sed <span class="more">[…]</span></p>
        <span class="read-more">CONTINUE READING
          <svg width="7" height="10" viewBox="0 0 7 10" aria-hidden="true"><path d="M1.5 1.5 L5 5 L1.5 8.5" stroke="var(--white)" stroke-width="2" fill="none"/></svg>
        </span>
      </article>

      <hr class="post-divider">

      <article class="post" style="top:631px">
        <h2 class="post-title">Links Post</h2>
        <div class="post-meta">
          <span>August 7, 2013, admin in Uncategorized</span>
          <span class="comments">
            <svg width="11" height="10" viewBox="0 0 11 10" aria-hidden="true"><ellipse cx="5.5" cy="4.5" rx="5.5" ry="4" fill="var(--meta)"/><path d="M2 7 L1 10 L5 8 Z" fill="var(--meta)"/></svg>
            Leave a comment
          </span>
        </div>
        <p class="post-excerpt">Lorem ipsum dolor sit amet, consectetur adipisicing elit, sed do eiusmod tempor incididunt ut labore et dolore magna aliqua. Ut enim ad minim veniam, quis nostrud exercitation ullamco laboris nisi ut aliquip ex ea commodo consequat. Duis aute irure dolor in reprehenderit in voluptate velit esse cillum dolore eu fugiat nulla pariatur. Excepteur sint occaecat cupidatat non proident.</p>
      </article>
    </main>
  </div>
</body>
</html>
```